Flyer-Design für Website & Softwareentwicklung
Zielgruppe
Velorant bietet Website & Software Entwicklung. Weitere Infos entnehmen Sie bitte der Webseite https://www.velorant-beispiel.de/
Aufgabenstellung
- Farben: Orientierung an Website/Logo
- Bilder: Entweder Sie nehmen eines von meiner Webseite oder machen Vorschläge aus Bilddatenbanken
- Logo: Bitte entfernern Sie den Text 'Programmierung, Optimierung und Gestaltung' aus dem Logo.
- Für den Aufbau und Design lasse ich Ihnen freie Gestaltungsmöglichkeiten
- Sinnvoll wäre ein Platz für einen kleinen Text, was Velorant genau macht
- Ebenfalls sollte irgendwie klar werden, dass wir ein lokales Unternehmen sind mit Sitz in Ketsch
- Sinnvoll wäre auch zum Beispiel die drei Services, welche auch auf unserer Webseite stehen, zu platzieren.
- Kontaktmöglichkeiten: Telefonat, E-Mail, Webadresse sollten auf jeden Fall drauf sein.
- Wenn Sie noch weitere Ideen haben, bin ich Ihnen sehr dankbar!
- Der Flyer wird am Ende bei Oberliga Nord Handballspielen ausgelegt, um Neukunden zu werben.

```html
<!DOCTYPE html>
<html lang="de">
<head>
<meta charset="utf-8">
<title>Velorant Flyer</title>
<link href="https://fonts.googleapis.com/css2?family=Roboto:wght@400;500;700&family=Lato:wght@400&display=swap" rel="stylesheet">
<style>
  :root {
    --green: #8dc63f;
    --green-dark: #7db83a;
    --ink: #2b2b2b;
    --grey: #8a8a8a;
    --page: #f4f4f4;
    --white: #ffffff;
  }
  * { margin: 0; padding: 0; box-sizing: border-box; }
  html, body { width: 1200px; height: 1054px; overflow: hidden; }
  body { background: var(--page); font-family: "Roboto", Arial, sans-serif; color: var(--ink); position: relative; }

  .flyer { position: absolute; left: 272px; top: 67px; width: 656px; height: 918px; background: var(--white); overflow: hidden; box-shadow: 0 6px 30px rgba(0,0,0,.06); }
  .shapes { position: absolute; inset: 0; }

  .brand { position: absolute; left: 30px; top: 296px; }
  .brand-name { display: flex; align-items: center; gap: 10px; font-family: "Roboto", Arial, sans-serif; font-weight: 400; font-size: 48px; letter-spacing: 1px; color: var(--grey); line-height: 1; }
  .brand-dot { width: 16px; height: 16px; border-radius: 50%; background: var(--green); }
  .brand-tagline { margin-top: 10px; font-family: "Lato", Arial, sans-serif; font-size: 7.6px; color: var(--grey); letter-spacing: .1px; }

  .headline { position: absolute; left: 30px; top: 423px; font-weight: 700; text-transform: uppercase; line-height: 1; }
  .headline .small { display: block; font-size: 18px; font-weight: 500; }
  .headline .large { display: block; font-size: 25.5px; margin-top: 4px; }
  .headline .mid { display: block; font-size: 18px; font-weight: 500; margin-top: 7px; }
  .headline .accent { display: block; font-size: 32px; color: var(--green); margin-top: 8px; }

  .why { position: absolute; left: 30px; top: 558px; width: 400px; }
  .why h2 { font-size: 15px; font-weight: 700; color: var(--green); text-transform: uppercase; }
  .why h3 { font-size: 11.2px; font-weight: 400; margin-top: 16px; }
  .why p { font-size: 11.2px; line-height: 14px; margin-top: 3px; }

  .services { position: absolute; left: 30px; top: 681px; width: 529px; height: 157px; display: flex; }
  .service { flex: 1; background: var(--green); color: var(--white); padding: 13px 14px 0 19px; position: relative; }
  .service--alt { background: var(--green-dark); }
  .service-icon { display: block; margin-left: auto; margin-right: 0; }
  .service h4 { font-size: 14.5px; font-weight: 700; margin-top: 8px; white-space: nowrap; }
  .service p { font-size: 9.3px; line-height: 13px; margin-top: 13px; }

  .contact { position: absolute; left: 0; top: 864px; width: 656px; height: 36px; background: var(--green); color: var(--white); font-size: 11.3px; }
  .contact span { position: absolute; top: 11px; }
  .contact .web { left: 67px; }
  .contact .mail { left: 196px; top: 10px; }
  .contact .phone { left: 339px; }
</style>
</head>
<body>
<main class="flyer">
  <svg class="shapes" width="656" height="918" viewBox="0 0 656 918">
    <defs>
      <linearGradient id="photoTone" x1="1" y1="0" x2="0" y2="1">
        <stop offset="0" stop-color="#6cc3b8"/>
        <stop offset=".35" stop-color="#5d8b92"/>
        <stop offset=".7" stop-color="#4f5b69"/>
        <stop offset="1" stop-color="#2d3540"/>
      </linearGradient>
    </defs>
    <path class="corner-triangle" d="M0 71 L96 170 Q104 180 96 190 L0 285 Z" fill="var(--green)"/>
    <path class="corner-band" d="M455 0 L656 0 L656 699 L478 533 L403 161 L356 114 Q345 103 356 92 Z" fill="var(--green)"/>
    <g role="img" aria-label="Foto: Hände auf einer Laptop-Tastatur vor einem Bildschirm mit Programmcode">
      <path d="M545 0 L656 0 L656 585 L622 615 Q610 626 598 614 L280 310 Q272 300 280 290 Z" fill="url(#photoTone)"/>
    </g>
    <path class="photo-tint" d="M656 135 L530 270 Q523 278 530 286 L656 435 Z" fill="var(--green)" opacity=".45"/>
  </svg>

  <div class="brand">
    <div class="brand-name"><span>Velorant</span><span class="brand-dot"></span></div>
    <div class="brand-tagline">Softwareentwicklung | Webentwicklung | Webdesign</div>
  </div>

  <h1 class="headline">
    <span class="small">Bringen Sie Ihr</span>
    <span class="large">Unternehmen auf ein</span>
    <span class="mid">neues Level von</span>
    <span class="accent">Erfolg</span>
  </h1>

  <section class="why">
    <h2>Warum uns wählen</h2>
    <h3>2015 Namensfindung</h3>
    <p>Der Name Velorant ergibt sich aus den Bestandteilen: Ve, Lo und Rant. Während die ersten beiden Silben für die Ideen des Gründers Thomas Bergel stehen, erklären die übrigen die Services, die Velorant bietet.</p>
  </section>

  <section class="services">
    <article class="service">
      <svg class="service-icon" width="34" height="34" viewBox="0 0 34 34" fill="none" stroke="#fff" stroke-width="1.3">
        <rect x="1" y="1" width="32" height="32"/><line x1="1" y1="8" x2="33" y2="8"/>
        <rect x="19" y="3" width="3" height="3"/><rect x="23.5" y="3" width="3" height="3"/><rect x="28" y="3" width="3" height="3"/>
        <text x="17" y="26" fill="#fff" stroke="none" font-size="12" text-anchor="middle" font-family="Roboto, sans-serif">API</text>
      </svg>
      <h4>Softwareentwicklung</h4>
      <p>Wir erstellen hochverfügbare, skalierbare, flexible, anpassbare und moderne Software in der Cloud.</p>
    </article>
    <article class="service service--alt">
      <svg class="service-icon" width="42" height="34" viewBox="0 0 42 34" fill="none" stroke="#fff" stroke-width="1.3">
        <rect x="1" y="1" width="40" height="32"/><line x1="1" y1="7" x2="41" y2="7"/>
        <rect x="6" y="11" width="4" height="18"/>
        <path d="M19 16 L15 20 L19 24 M32 16 L36 20 L32 24 M27 15 L24 25"/>
      </svg>
      <h4>Webentwicklung</h4>
      <p>Wir programmieren jede denkbare Webseite von klein bis groß. Sie haben eine Idee? Profitieren Sie von unserem Wissen.</p>
    </article>
    <article class="service">
      <svg class="service-icon" width="42" height="42" viewBox="0 0 42 42" fill="none" stroke="#fff" stroke-width="1.3">
        <rect x="1" y="1" width="38" height="28"/><line x1="1" y1="6" x2="39" y2="6"/>
        <path d="M5 10 H20 M5 14 H24 V19 H5 Z M5 23 H18"/>
        <path d="M30 20 L38 36 Q40 40 36 38 L28 22 Z"/>
      </svg>
      <h4>Webdesign</h4>
      <p>Wir konzipieren, gestalten und entwickeln moderne und einzigartige Webseiten und Online-Shops mit responsive Web Design!</p>
    </article>
  </section>

  <footer class="contact">
    <span class="web">www.velorant-beispiel.de</span>
    <span class="mail">E: info@velorant-beispiel.de</span>
    <span class="phone">C: +49 170 5550 1834</span>
  </footer>
</main>
</body>
</html>
```